Website Redesign Brief for Breezeline Cooling Services WA

Creating a clear and concise brief for designers to redesign your website, https://breezelinecoolingwa.com.au/, is essential to ensure the project aligns with your vision for a more energetic, friendly, optimistic, and user-friendly website. Below is a sample brief tailored to your request, balancing specificity with flexibility to allow designers to bring their creativity to the table.

Website Redesign Brief for Breezeline Cooling WA
1. Project Overview

We are seeking a redesign of our website, https://breezelinecoolingwa.com.au/, to create a vibrant, engaging, and user-friendly online presence that reflects our brand’s commitment to providing top-notch air conditioning services in Western Australia. The redesigned website should feel energetic, friendly, and optimistic while maintaining professionalism and improving user experience.
2. Goals and Objectives

Enhance Brand Perception: Convey a modern, approachable, and positive brand identity that resonates with both residential and commercial clients.
Improve User Experience: Simplify navigation, improve accessibility, and ensure a seamless experience across devices (desktop, tablet, mobile).
Increase Engagement: Encourage visitors to explore services, request quotes, and contact us through clear calls-to-action (CTAs).
Boost Conversion Rates: Make it easier for users to find information and take action (e.g., booking services or inquiries).
Showcase Expertise: Highlight our professional air conditioning services, experience, and customer satisfaction in an inviting way.

3. Target Audience

Primary Audience: Homeowners and small business owners in Western Australia seeking air conditioning installation, maintenance, or repair services.
Secondary Audience: Property managers, commercial clients, and real estate professionals looking for reliable HVAC solutions.
Demographics: Ages 25–65, mix of tech-savvy and non-tech-savvy users, located primarily in Perth and surrounding areas.
User Needs: Clear information about services, transparent pricing, easy contact options, and reassurance of quality and reliability.

4. Design Preferences

Tone and Style:

Energetic: Use bold, vibrant colors (e.g., blues, whites, and pops of warm tones like orange or yellow) to evoke energy and optimism.
Friendly: Incorporate approachable language, welcoming imagery, and a clean, uncluttered layout.
Optimistic: Highlight positive customer outcomes (e.g., comfort, energy savings) through visuals and messaging.
Professional yet approachable: Maintain credibility as a trusted service provider while avoiding a cold or overly corporate feel.

Visual Elements:

Use high-quality images of happy customers, comfortable homes/offices, and modern air conditioning units.
Incorporate subtle animations or micro-interactions to add energy (e.g., hover effects on buttons or smooth scrolling).
Avoid overly complex graphics that may slow down the site or distract from usability.

Typography: Clean, modern fonts that are easy to read. Use larger, bold headings for hierarchy and warmth.
Inspiration: Websites like https://www.polarvane.com.au/ (clean and professional) or https://www.kestrelthermaltech.com.au/ (user-friendly and modern) but with a more vibrant and welcoming vibe.

5. Functional Requirements

User-Friendly Navigation: Simplify the menu structure to make key pages (e.g., Services, About Us, Contact) easily accessible.
Mobile Responsiveness: Ensure the site is fully optimized for mobile devices, with fast load times and intuitive touch interactions.
Key Features:

Prominent CTAs for requesting quotes, booking services, or contacting the team.
A clear service overview with icons or visuals for each service (e.g., installation, repairs, maintenance).
A testimonials section to showcase customer satisfaction.
An easy-to-use contact form with minimal fields.
Integration with Google Maps for location-based services or office directions.

SEO and Performance: Optimize for search engines (e.g., keywords like “air conditioning Perth”) and ensure fast loading speeds.
Accessibility: Follow WCAG guidelines to ensure the site is usable for all visitors, including those with disabilities.

6. Content Guidance

Existing Content: Review and refine current content from https://breezelinecoolingwa.com.au/ to make it concise, engaging, and aligned with the friendly tone.
New Content Ideas:

Add a “Why Choose Us” section highlighting expertise, customer service, and eco-friendly solutions.
Include a FAQ page to address common customer questions.
Create a blog section for tips on air conditioning maintenance or energy efficiency (optional).

Tone of Voice: Conversational, reassuring, and positive. Avoid technical jargon unless clearly explained.

7. Technical Considerations

Platform: Open to recommendations (e.g., WordPress, Wix, or custom-built) but prioritize ease of maintenance and scalability.
Integrations: Ensure compatibility with existing tools (e.g., Google Analytics, CRM for quote requests, or booking systems).
Domain and Hosting: Retain current domain (breezelinecoolingwa.com.au); hosting recommendations welcome.
Timeline: Initial design concepts within [insert timeline, e.g., 2–3 weeks], with full redesign completed by [insert deadline, e.g., 6–8 weeks].
Budget: [Insert budget range or state “flexible, please provide a quote”].

8. Deliverables

Wireframes and mockups for homepage, service pages, and contact page.
Fully responsive website design with all necessary pages.
Style guide (colors, fonts, imagery guidelines).
CMS setup (if applicable) with basic training for content updates.
Testing and optimization for performance and SEO.

9. Success Metrics

Increased time on site and reduced bounce rate.
Higher conversion rates for quote requests and contact form submissions.
Positive user feedback on ease of navigation and overall experience.
Improved search engine rankings for key terms within [insert timeframe, e.g., 3 months].

10. Additional Notes

Please provide a portfolio of similar projects or examples of user-friendly, vibrant websites.
We are open to creative suggestions to make the website stand out in the HVAC industry.
Regular progress updates and collaboration during the design process are appreciated.
Updates

designers are asking for more time

few have requested an extension. I Have extended

Target Market(s)

Primary Audience: Homeowners and small business owners in Western Australia seeking air conditioning installation, maintenance, or repair services. Secondary Audience: Property managers, commercial clients, and real estate professionals looking for reliable HVAC solutions. Demographics: Ages 25–65, mix of tech-savvy and non-tech-savvy users, located primarily in Perth and surrounding areas. User Needs: Clear information about services, transparent pricing, easy contact options, and reassurance of quality and reliability.

Industry/Entity Type

Air Conditioning and Refrigeration (HVAC & R)

Coding

Coded - Design and coding required

Colors
0054AA
0677BA
7BADD7
CADEEF
E8F1F8
59FF00
82FF00
B8FF75
E3FFCB
F4FFEA
F0912C
F2A743
F7CA91
FBE8D2
FDF5EE
EE7325
F08F49
F5BC92
FAE3D3
FDF4ED

Requirements
Must have
• Must have all my current information I currently have on my web page.
Nice to have
• A sales page for people to buy products online

```html
<!DOCTYPE html>
<html lang="en">
<head>
<meta charset="utf-8">
<title>Mastering The First Impression – Tidecrest Cooling WA</title>
<link rel="stylesheet" href="https://fonts.googleapis.com/css2?family=Montserrat:wght@500;600;700&family=Figtree:wght@400;500;600;700&family=Roboto:wght@400;500&display=swap">
<style>
  :root {
    --ink: #1b1b1b;
    --body: #3d4248;
    --panel: #e8f1f8;
    --page: #ffffff;
    --accent: #f0591a;
    --accent-red: #e3141c;
    --adminbar: #1d2327;
    --adminbar-text: #f0f0f1;
    --rule: #cfd6dc;
  }
  * { box-sizing: border-box; margin: 0; padding: 0; }
  html, body { width: 1200px; height: 2647px; overflow: hidden; background: var(--page); }
  body { position: relative; font-family: "Figtree", sans-serif; color: var(--body); }

  .admin-bar { position: absolute; top: 0; left: 0; width: 1200px; height: 27px; background: var(--adminbar);
    color: var(--adminbar-text); font: 400 11px "Roboto", sans-serif; display: flex; align-items: center; padding: 0 8px; }
  .admin-bar .item { display: flex; align-items: center; gap: 5px; margin-right: 15px; }
  .admin-bar .dot { width: 16px; height: 16px; border-radius: 50%; border: 2px solid #a7aaad; }
  .admin-bar svg { fill: #a7aaad; }
  .admin-bar .right { margin-left: auto; display: flex; align-items: center; gap: 10px; }
  .admin-bar .avatar { width: 14px; height: 14px; background: #c3c4c7; }

  .site-header { position: absolute; top: 27px; left: 0; width: 1200px; height: 130px; }
  .brand { position: absolute; left: 112px; top: 32px; display: flex; align-items: center; gap: 28px; }
  .brand-mark { width: 58px; height: 58px; border-radius: 50%; background: var(--accent); margin-left: 12px; }
  .brand-name { font: 700 22px "Montserrat", sans-serif; color: var(--ink); }
  .main-nav { position: absolute; left: 587px; top: 55px; display: flex; gap: 31px; font: 400 14.5px "Figtree", sans-serif; color: var(--ink); }
  .quote-btn { position: absolute; left: 950px; top: 45px; width: 161px; height: 38px; border: 2px solid var(--ink);
    border-radius: 20px; display: flex; align-items: center; justify-content: center;
    font: 700 12px "Montserrat", sans-serif; color: var(--ink); }

  .panel { position: absolute; left: 307px; width: 598px; background: var(--panel); padding: 34px; }
  .article { top: 209px; height: 1325px; }
  .post-title { font: 700 27.5px/32px "Montserrat", sans-serif; color: var(--ink); letter-spacing: -0.5px; }
  .post-meta { display: flex; align-items: center; gap: 5px; margin-top: 22px; font: 600 11px "Figtree", sans-serif; color: #333; }
  .post-meta .avatar { width: 34px; height: 34px; border-radius: 50%; background: #d7d9dc; border: 2px solid #fff; margin-left: 4px; }
  .post-meta .author { color: var(--accent); font-weight: 500; }
  .featured-image { width: 530px; height: 397px; margin-top: 18px;
    background: linear-gradient(100deg, #d9c9c4 0%, #eef0f1 25%, #f7f8f8 55%, #e1e6e8 80%, #cfd7d8 100%); }
  .article h2 { font: 600 20px/25px "Montserrat", sans-serif; color: var(--ink); margin-top: 32px; letter-spacing: -0.3px; }
  .article h2.gap { margin-top: 43px; }
  .article p { font: 400 14.3px/23px "Figtree", sans-serif; margin-top: 13px; }

  .post-nav { position: absolute; left: 309px; top: 1562px; width: 596px; }
  .post-nav .label { font: 700 12px "Figtree", sans-serif; color: var(--ink); letter-spacing: .4px; display: flex; align-items: center; gap: 4px; }
  .post-nav .link { font: 400 14.5px "Figtree", sans-serif; color: var(--ink); margin-top: 8px; }
  .post-nav .divider { position: absolute; left: 297px; top: 13px; width: 1px; height: 26px; background: var(--rule); }

  .related { top: 1639px; height: 427px; }
  .related h2 { font: 600 27px "Montserrat", sans-serif; color: var(--ink); margin-top: 4px; letter-spacing: -0.3px; }
  .related-grid { display: flex; gap: 36px; margin-top: 220px; }
  .related-card { width: 240px; }
  .related-card h3 { font: 700 16.5px/22px "Montserrat", sans-serif; color: var(--ink); letter-spacing: -0.3px; }
  .related-card .meta { font: 600 11.5px "Figtree", sans-serif; color: var(--accent-red); margin-top: 9px; }

  .comments { top: 2094px; height: 431px; }
  .comments h3 { font: 600 18px "Montserrat", sans-serif; color: var(--ink); margin-top: 5px; }
  .comments .logged { font: 400 14.3px "Figtree", sans-serif; color: #333; margin-top: 20px; }
  .comments .logged span { color: var(--accent-red); }
  .comment-box { width: 530px; height: 183px; margin-top: 16px; background: #fff; border: 1px solid #444;
    padding: 13px 14px; font: 400 14px "Figtree", sans-serif; color: #8a8f95; }
  .post-btn { width: 166px; height: 44px; margin-top: 30px; border-radius: 22px; background: var(--accent);
    color: #fff; font: 700 13px "Montserrat", sans-serif; display: flex; align-items: center; justify-content: center; }

  .site-footer { position: absolute; top: 2601px; left: 101px; width: 1010px; display: flex; justify-content: space-between;
    font: 400 14.5px "Figtree", sans-serif; color: var(--ink); }
  .footer-nav { display: flex; gap: 14px; }
</style>
</head>
<body>

<div class="admin-bar">
  <div class="item"><span class="dot"></span></div>
  <div class="item">Tidecrest Cooling WA</div>
  <div class="item">
    <svg width="12" height="12" viewBox="0 0 12 12"><path d="M9 1l2 2-6 6-3 1 1-3z"/></svg>Customize
  </div>
  <div class="item">
    <svg width="12" height="12" viewBox="0 0 12 12"><path d="M1 1h10v7H5l-3 3V8H1z"/></svg>0
  </div>
  <div class="item">
    <svg width="11" height="11" viewBox="0 0 11 11"><path d="M4.5 0h2v4.5H11v2H6.5V11h-2V6.5H0v-2h4.5z"/></svg>New
  </div>
  <div class="item">
    <svg width="12" height="12" viewBox="0 0 12 12"><path d="M9 1l2 2-6 6-3 1 1-3z"/></svg>Edit Post
  </div>
  <div class="item">Formvane</div>
  <div class="right">
    <svg width="16" height="16" viewBox="0 0 16 16"><path d="M8 1l1.5 5L14 8l-4.5 2L8 15l-1.5-5L2 8l4.5-2z"/></svg>
    <span>Howdy, admin</span><span class="avatar"></span>
  </div>
</div>

<header class="site-header">
  <div class="brand">
    <span class="brand-mark"></span>
    <span class="brand-name">Tidecrest Cooling WA</span>
  </div>
  <nav class="main-nav">
    <span>Home</span><span>About</span><span>Services</span><span>Blog</span><span>Contact</span>
  </nav>
  <div class="quote-btn">REQUEST A QUOTE</div>
</header>

<article class="panel article">
  <h1 class="post-title">Mastering The First Impression: Your Intriguing Post Title Goes Here</h1>
  <div class="post-meta">
    <span class="avatar"></span>By <span class="author">admin</span> / August 15, 2025
  </div>
  <div class="featured-image" role="img" aria-label="White window air conditioning unit beside window blinds"></div>

  <h2>Engaging Introductions: Capturing Your Audience’s Interest</h2>
  <p>The initial impression your blog post makes is crucial, and that’s where your introduction comes into play. Hook your readers with a captivating opening that sparks curiosity or emotion. Address their pain points or questions to establish a connection. Outline the purpose of your post and give a sneak peek into what they can expect. A well-crafted introduction sets the tone for an immersive reading experience.</p>

  <h2 class="gap">Crafting Informative And Cohesive Body Content</h2>
  <p>Within the body of your blog post lies the heart of your message. Break down your content into coherent sections, each with a clear heading that guides readers through the narrative. Dive deep into each subtopic, providing valuable insights, data, and relatable examples. Maintain a logical flow between paragraphs using transitions, ensuring that each point naturally progresses to the next. By structuring your body content effectively, you keep readers engaged and eager to learn more.</p>

  <h2 class="gap">Powerful Closures: Leaving A Lasting Impression</h2>
  <p>Concluding your blog post isn’t just about wrapping things up – it’s your final opportunity to leave a strong impact. Summarize the key takeaways from your post, reinforcing your main points. If relevant, provide actionable solutions or thought-provoking questions to keep readers thinking beyond the post. Encourage engagement by inviting comments, questions, or sharing. A well-crafted conclusion should linger in your readers’ minds, inspiring them to explore further or apply what they’ve learned.</p>
</article>

<nav class="post-nav">
  <div class="label">
    <svg width="12" height="8" viewBox="0 0 12 8"><path d="M4 0L0 4l4 4V5h8V3H4z" fill="#1b1b1b"/></svg>PREVIOUS
  </div>
  <div class="link">Hello world!</div>
  <span class="divider"></span>
</nav>

<section class="panel related">
  <h2>Related Posts</h2>
  <div class="related-grid">
    <div class="related-card">
      <h3>The Art Of Drawing Readers In: Your Attractive Post Title Goes Here</h3>
      <div class="meta">August 15, 2025 / General / By admin</div>
    </div>
    <div class="related-card">
      <h3>Crafting Captivating Headlines: Your Awesome Post Title Goes Here</h3>
      <div class="meta">August 15, 2025 / General / By admin</div>
    </div>
  </div>
</section>

<section class="panel comments">
  <h3>Leave A Comment</h3>
  <p class="logged">Logged in as admin. <span>Edit your profile.</span> <span>Log out?</span> Required fields are marked *</p>
  <div class="comment-box">Type here..</div>
  <div class="post-btn">POST COMMENT</div>
</section>

<footer class="site-footer">
  <nav class="footer-nav"><span>Home</span><span>About</span><span>Services</span><span>Blog</span><span>Contact</span></nav>
  <span>Copyright © 2025 Tidecrest Cooling WA</span>
</footer>

</body>
</html>
```